Small Business Consulting Firm Needs Business Card Design

Need a sleek modern business card with 2 sides matching the colors of our logo. We will be placing these with a mailer we are sending out. These business cards will only ever be given to business owners. We operate helping businesses who are struggling with cash flow or finances. If the green and blue design needs to be moved to the right of "Brightpath Ledger Consulting" for aesthetic purposes that is ok. We will need an editable file if possible. We would like to include the reps name, email, website, and phone number. For now just use Owen Parrish, oparrish@brightpathledger.com, www.brightpathledger.com, and 855-219-7038.

```html
<!DOCTYPE html>
<html lang="en">
<head>
<meta charset="utf-8">
<title>Brightpath Ledger Consulting – Business Card</title>
<link href="https://fonts.googleapis.com/css2?family=Montserrat:wght@300;400;500&display=swap" rel="stylesheet">
<style>
  :root {
    --backdrop: #3a3b3d;
    --card-white: #ffffff;
    --brand-blue: #1467b3;
    --brand-green: #5f9f38;
    --grad-blue: #13599a;
    --grad-teal: #2f7a7e;
    --grad-green: #6aa23a;
    --ink: #3b3c3e;
    --ink-soft: #555759;
  }
  * { margin: 0; padding: 0; box-sizing: border-box; }
  html, body { width: 1200px; height: 900px; overflow: hidden; }
  body {
    background: var(--backdrop);
    font-family: "Montserrat", Arial, sans-serif;
    display: flex;
    flex-direction: column;
    align-items: center;
    justify-content: center;
    gap: 56px;
  }
  .card {
    width: 600px;
    height: 343px;
    border-radius: 3px;
    position: relative;
    overflow: hidden;
    box-shadow: 0 10px 24px rgba(0,0,0,0.35);
  }

  /* Front */
  .card-front {
    background: linear-gradient(30deg, var(--grad-blue) 0%, var(--grad-teal) 50%, var(--grad-green) 100%);
    display: flex;
    flex-direction: column;
    align-items: center;
    justify-content: center;
    color: #ffffff;
  }
  .brand-mark {
    width: 54px;
    height: 54px;
    background: #ffffff;
    margin-bottom: 24px;
  }
  .brand-name {
    font-weight: 300;
    text-align: center;
    letter-spacing: 1px;
    line-height: 1.25;
  }
  .brand-name .primary { display: block; font-size: 28px; text-transform: uppercase; }
  .brand-name .secondary { display: block; font-size: 13px; letter-spacing: 7px; text-transform: uppercase; }

  /* Back */
  .card-back {
    background: var(--card-white);
    display: flex;
    align-items: center;
    padding: 0 40px 0 44px;
  }
  .back-brand {
    width: 250px;
    display: flex;
    flex-direction: column;
    align-items: center;
    color: var(--ink);
  }
  .back-brand .brand-mark { background: var(--brand-green); margin-bottom: 18px; }
  .back-brand .primary { font-size: 21px; }
  .back-brand .secondary { font-size: 10px; letter-spacing: 5px; }
  .divider {
    width: 1.5px;
    height: 150px;
    background: var(--brand-blue);
    margin: 0 26px 0 22px;
  }
  .contact { color: var(--ink); }
  .rep-name {
    font-size: 18px;
    font-weight: 500;
    color: var(--brand-blue);
    letter-spacing: 1px;
    text-transform: uppercase;
  }
  .rep-title { font-size: 12px; color: var(--ink-soft); margin: 4px 0 20px; }
  .contact-list { list-style: none; font-size: 14px; }
  .contact-list li { display: flex; align-items: center; gap: 10px; margin-bottom: 8px; }
  .contact-list svg { width: 17px; height: 17px; flex: none; fill: var(--brand-blue); }
</style>
</head>
<body>

  <section class="card card-front">
    <div class="brand-mark"></div>
    <h1 class="brand-name">
      <span class="primary">Brightpath Ledger</span>
      <span class="secondary">Consulting</span>
    </h1>
  </section>

  <section class="card card-back">
    <div class="back-brand">
      <div class="brand-mark"></div>
      <h2 class="brand-name">
        <span class="primary">Brightpath Ledger</span>
        <span class="secondary">Consulting</span>
      </h2>
    </div>
    <div class="divider"></div>
    <div class="contact">
      <p class="rep-name">Owen Parrish</p>
      <p class="rep-title">CEO | Founder</p>
      <ul class="contact-list">
        <li>
          <svg viewBox="0 0 24 24" aria-hidden="true"><path d="M6.6 10.8a15.1 15.1 0 0 0 6.6 6.6l2.2-2.2a1 1 0 0 1 1-.25 11.4 11.4 0 0 0 3.6.57 1 1 0 0 1 1 1V20a1 1 0 0 1-1 1A17 17 0 0 1 3 4a1 1 0 0 1 1-1h3.5a1 1 0 0 1 1 1c0 1.25.2 2.45.57 3.57a1 1 0 0 1-.25 1z"/></svg>
          855 219 7038
        </li>
        <li>
          <svg viewBox="0 0 24 24" aria-hidden="true"><path d="M2 5h20v14H2z M2 5l10 8 10-8" /><path d="M2 6.5l10 7.5 10-7.5V5H2z" fill="#ffffff"/></svg>
          oparrish@brightpathledger.com
        </li>
        <li>
          <svg viewBox="0 0 24 24" aria-hidden="true"><circle cx="12" cy="12" r="10"/><path d="M2.5 12h19M12 2c3 3 3 17 0 20M12 2c-3 3-3 17 0 20" stroke="#ffffff" stroke-width="1.4" fill="none"/></svg>
          www.brightpathledger.com
        </li>
      </ul>
    </div>
  </section>

</body>
</html>
```